Label/ sleeve for olive oil tin can

We are looking for a design of a full sleeve label for our olive oil cans. These cans contain 500ml of oil and the label should have a dimension of approximately 215mm wide and 175mm high.

Please find the first draft of the design guidelines attached as well as the brand logo.
Updates

Low design quality

Target Market(s)

Consumers

Industry/Entity Type

Olive oil

Colors
00AB8E
00BBA5
67D7C9
C6EFE9
E9F9F6

Requirements
Must have
• Full label design - around the entire bottle. Read the brief

```html
<!DOCTYPE html>
<html lang="en">
<head>
<meta charset="utf-8">
<title>Villa Solmeria – Extra Virgin Olive Oil Sleeve</title>
<link rel="stylesheet" href="https://fonts.googleapis.com/css2?family=Montserrat:wght@400;500;600&family=Roboto+Condensed:wght@400;500&display=swap">
<style>
  :root {
    --page: #eef1f4;
    --sleeve-light: #c6efe9;
    --sleeve-mid: #8fe0d8;
    --sleeve-deep: #67d7c9;
    --panel-top: #0a7f93;
    --panel-bottom: #055a6c;
    --gold: #d8b562;
    --gold-deep: #b08a3a;
    --ink: #0d3b44;
    --white: #ffffff;
    --tree-dark: #1f5a63;
    --tree-light: #5fb8b4;
  }
  * { margin: 0; padding: 0; box-sizing: border-box; }
  html, body { width: 1200px; height: 878px; overflow: hidden; }
  body {
    background: var(--page);
    display: flex; align-items: center; justify-content: center;
    font-family: "Montserrat", sans-serif;
  }
  .sleeve {
    position: relative;
    width: 860px; height: 700px;
    background: linear-gradient(90deg, var(--sleeve-deep) 0%, var(--sleeve-light) 45%, var(--sleeve-mid) 100%);
    overflow: hidden;
    box-shadow: 0 10px 30px rgba(13, 59, 68, 0.15);
  }
  .brand-panel {
    position: absolute; left: 215px; top: 0;
    width: 430px; height: 430px;
  }
  .brand-panel svg { display: block; }
  .brand-name {
    position: absolute; left: 0; right: 0; top: 96px;
    text-align: center;
    font-size: 50px; font-weight: 500; color: var(--gold);
    letter-spacing: 0.5px;
    display: flex; align-items: center; justify-content: center; gap: 14px;
  }
  .brand-dot {
    width: 22px; height: 22px; border-radius: 50%;
    background: var(--gold); display: inline-block;
  }
  .brand-tagline {
    position: absolute; left: 0; right: 0; top: 168px;
    text-align: center;
    font-family: "Roboto Condensed", sans-serif;
    font-size: 17px; color: var(--white); letter-spacing: 0.3px;
  }
  .olive {
    position: absolute; left: 188px; top: 210px;
    width: 54px; height: 44px; border-radius: 50%;
    background: radial-gradient(circle at 35% 35%, #b9c64a, #5f7a1d 80%);
  }
  .greek-title {
    position: absolute; left: 430px; top: 452px;
    font-size: 20px; font-weight: 500; color: var(--ink); letter-spacing: 1px;
  }
  .origin-line {
    position: absolute; left: 430px; top: 482px;
    font-family: "Roboto Condensed", sans-serif;
    font-size: 14px; color: var(--ink);
  }
  .tree-art {
    position: absolute; left: 110px; top: 430px;
    width: 300px; height: 270px;
    border-radius: 48% 52% 8% 8% / 60% 60% 4% 4%;
    background: radial-gradient(ellipse at 50% 35%, var(--tree-light) 0%, var(--tree-dark) 85%);
    opacity: 0.85;
  }
  .bottom-info {
    position: absolute; left: 430px; top: 560px;
    display: flex; align-items: center; gap: 22px;
    color: var(--ink);
  }
  .pressing {
    font-family: "Roboto Condensed", sans-serif;
    font-size: 15px; line-height: 1.35; font-weight: 500;
    padding-right: 22px; border-right: 1px solid var(--ink);
  }
  .organic-seal {
    width: 70px; height: 70px; border-radius: 50%;
    background: radial-gradient(circle at 40% 35%, #f0d78d, var(--gold-deep));
  }
  .volume { font-family: "Roboto Condensed", sans-serif; }
  .volume .amount { font-size: 22px; font-weight: 500; display: block; }
  .volume .note { font-size: 14px; }
</style>
</head>
<body>
  <main class="sleeve">
    <section class="brand-panel">
      <svg width="430" height="430" viewBox="0 0 430 430" aria-hidden="true">
        <defs>
          <linearGradient id="panelFill" x1="0" y1="0" x2="0" y2="1">
            <stop offset="0" stop-color="var(--panel-top)"/>
            <stop offset="1" stop-color="var(--panel-bottom)"/>
          </linearGradient>
          <path id="labelArc" d="M 70 265 A 145 145 0 0 0 360 265"/>
        </defs>
        <path d="M 6 0 L 6 215 A 209 209 0 0 0 424 215 L 424 0 Z" fill="url(#panelFill)" stroke="var(--gold)" stroke-width="5"/>
        <text font-family="Montserrat, sans-serif" font-size="24" font-weight="500" fill="#ffffff" letter-spacing="2">
          <textPath href="#labelArc" startOffset="50%" text-anchor="middle">EXTRA VIRGIN OLIVE OIL</textPath>
        </text>
      </svg>
      <div class="brand-name"><span class="brand-dot"></span>Villa Solmeria</div>
      <p class="brand-tagline">Holiday Rental &amp; Extra-Virgin Olive Oil</p>
      <div class="olive" role="img" aria-label="Green olive with leaf"></div>
    </section>

    <h2 class="greek-title">ΕΞΤΡΑ ΠΑΡΘΕΝΟ ΕΛΑΙΟΛΑΔΟ</h2>
    <p class="origin-line">From Villa Solmeria's olive trees on Zakynthos island</p>

    <div class="tree-art" role="img" aria-label="Engraved illustration of an ancient olive tree"></div>

    <div class="bottom-info">
      <p class="pressing">FIRST COLD PRESSING<br>ΠΡΩΤΟ ΨΥΧΡΟ ΠΙΕΣΗ</p>
      <div class="organic-seal" role="img" aria-label="Organic certification seal"></div>
      <p class="volume"><span class="amount">500 mL</span><span class="note">Limited Production</span></p>
    </div>
  </main>
</body>
</html>
```